Bold Vehicle Wrap Design for 2025 Halvorsen Trekmule Cargo Van

We need a full wrap design for our 2025 Halvorsen-Kraft Trekmule 2500 High Roof Cargo Van. This van will be used to represent Brightmark Pro Services, and we want it to stand out with a bold, professional look.

Vehicle Details:
2025 Trekmule 2500
High Roof
144" Wheelbase
Cargo configuration (no windows)

Our current logo is black, white, and gray — but we’re open to more colorful wrap concepts that could even influence a logo recolor.

We want a wrap design that:
Looks bold and professional
Incorporates icons for the services we provide:Plumbing,Handyman, Land Management, Junk and Debris Removal
Incorporates or complements our current logo
Avoids placing critical text or graphics across sliding doors, seams, or complex panel curves
Download all project files (template, logo, reference images):
https://files.quillbarn-share.com/f/7kq2vz9xw4nm18pd5r/BXTLUmQeKsPOtvc3h8rjnZW?key=2pxd9mwq47vbt6c5ls0eyhz3f&s=k8m3vqrt&dl=0

Target Market(s)

ocal residential and commercial customers in need of professional plumbing, handyman, land management, and junk/debris removal services. Homeowners and property managers looking for reliable and skilled service providers. Businesses and contractors who require prompt, professional, and trustworthy support for their facilities and properties. Customers who value quality workmanship and clear branding that conveys professionalism and expertise.

Industry/Entity Type

Local Service Providers specializing in residential and commercial property maintenance

Requirements
Must have
• Incorporate the Brightmark Pro Services logo with flexibility for adding color to complement the wrap. Use bold, professional, and eye-catching colors that stand out on the road. Include icons or visuals representing these key services: Plumbing Handyman Land Management Junk and Debris Removal. Design must fit a 2025 Halvorsen Trekmule 2500 High Roof Cargo Van (144" WB, cargo version with sliding door) — avoid placing important graphics or text over the sliding door seams or complex curves. Use high-contrast text and graphics for maximum readability from a distance. Design should be modern and clean, but bold enough to be memorable. Wrap design must work on all visible sides: driver side, passenger side, rear, and front. Provide final deliverables in Adobe Illustrator (.ai) or Photoshop (.psd) with layered files.
Nice to have
• Mockup images showing the wrap applied to the van template.
Should not have
• Do not place important text, logos, or graphics across the sliding door seam or uneven panel curves — they may get distorted or hidden.No low-contrast text or graphics that make information hard to read from a distance.Do not include any unrelated images or icons that don’t represent Brightmark Pro Services’ core offerings.Do not create a design that looks too similar to competitors or other well-known brands. No fonts that are hard to read or too decorative for a work vehicle.

```html
<!DOCTYPE html>
<html lang="en">
<head>
<meta charset="utf-8">
<title>Brightmark Pro Services – Van Wrap Side Panel</title>
<link href="https://fonts.googleapis.com/css2?family=Montserrat:wght@500;600;700;800&display=swap" rel="stylesheet">
<style>
  :root {
    --backdrop: #1e1e1e;
    --wrap-navy: #193f6e;
    --wrap-orange: #de4428;
    --wrap-white: #ffffff;
    --icon-navy: #1c3f70;
  }
  html, body {
    margin: 0;
    padding: 0;
    width: 1200px;
    height: 1199px;
    overflow: hidden;
    background: var(--backdrop);
  }
  .canvas {
    position: relative;
    width: 1200px;
    height: 1199px;
    display: flex;
    align-items: center;
    justify-content: center;
  }
  .wrap-panel {
    width: 1120px;
    height: 486px;
    display: block;
  }
  .wrap-panel text { font-family: "Montserrat", Arial, sans-serif; }
  .band-title { fill: var(--wrap-white); font-weight: 500; font-size: 68px; }
  .brand-name { fill: var(--wrap-white); font-weight: 800; }
  .brand-sub { fill: var(--wrap-white); font-weight: 500; }
  .service-label { fill: var(--wrap-white); font-weight: 600; font-size: 26px; }
  .service-label--small { font-size: 21px; }
  .service-pill { fill: var(--wrap-orange); }
  .service-icon-box { fill: var(--icon-navy); stroke: var(--wrap-orange); stroke-width: 3; }
  .icon-stroke { fill: none; stroke: var(--wrap-white); stroke-width: 2.6; stroke-linecap: round; stroke-linejoin: round; }
  .contact-phone { fill: var(--wrap-navy); font-weight: 600; font-size: 32px; }
  .contact-web { fill: var(--wrap-orange); font-weight: 500; font-size: 26px; }
  .contact-icon--phone { fill: none; stroke: var(--wrap-navy); stroke-width: 2; }
  .contact-icon--web { fill: none; stroke: var(--wrap-orange); stroke-width: 2; }
</style>
</head>
<body>
<main class="canvas">
  <svg class="wrap-panel" viewBox="0 0 1534 665" xmlns="http://www.w3.org/2000/svg" aria-label="Brightmark Pro Services van wrap, side panel layout">
    <rect class="field-navy" x="0" y="0" width="1534" height="665" fill="var(--wrap-navy)"/>
    <path class="top-band" d="M0,0 H1156 L930,118 Q905,133 870,133 H0 Z" fill="var(--wrap-orange)"/>
    <path class="lower-swoosh" d="M0,448 C250,385 600,375 820,440 C920,470 990,560 1015,665 L0,665 Z" fill="var(--wrap-orange)"/>
    <path class="lower-field" d="M0,458 C250,415 560,410 720,450 C860,490 960,570 1002,665 L0,665 Z" fill="var(--wrap-white)"/>

    <text class="band-title" x="100" y="104">Brightmark Pro Services</text>

    <g class="brand-lockup">
      <text class="brand-name" x="70" y="228" font-size="84" textLength="490" lengthAdjust="spacingAndGlyphs">BRIGHTMARK</text>
      <text class="brand-sub" x="70" y="272" font-size="36" textLength="290" lengthAdjust="spacingAndGlyphs">PRO SERVICES</text>
    </g>

    <g class="service-list">
      <g class="service service--plumbing">
        <rect class="service-pill" x="582" y="152" width="215" height="42" rx="6"/>
        <rect class="service-icon-box" x="584" y="154" width="50" height="38" rx="5"/>
        <path class="icon-stroke" d="M594,166 V182 M594,170 H618 Q624,170 624,177 V181 M605,163 V170 M600,163 H610"/>
        <text class="service-label" x="649" y="182">Plumbing</text>
      </g>
      <g class="service service--handyman">
        <rect class="service-pill" x="582" y="199" width="212" height="40" rx="6"/>
        <rect class="service-icon-box" x="584" y="201" width="50" height="36" rx="5"/>
        <path class="icon-stroke" d="M597,207 L622,231 M622,207 L597,231 M593,211 L601,203"/>
        <text class="service-label" x="638" y="228">Handyman</text>
      </g>
      <g class="service service--land">
        <rect class="service-pill" x="582" y="246" width="308" height="41" rx="6"/>
        <rect class="service-icon-box" x="584" y="248" width="50" height="37" rx="5"/>
        <path class="icon-stroke" d="M598,279 L609,262 L620,279 Z M609,262 V253 M603,257 Q609,250 615,257"/>
        <text class="service-label" x="638" y="276">Land Management</text>
      </g>
      <g class="service service--junk">
        <rect class="service-pill" x="582" y="291" width="308" height="42" rx="6"/>
        <rect class="service-icon-box" x="584" y="293" width="50" height="38" rx="5"/>
        <path class="icon-stroke" d="M599,303 H619 M606,300 H612 M601,306 L603,326 H615 L617,306 M606,310 V322 M612,310 V322"/>
        <text class="service-label service-label--small" x="640" y="318">Junk &amp; Debris Removal</text>
      </g>
    </g>

    <g class="contact">
      <circle class="contact-icon--phone" cx="442" cy="468" r="13"/>
      <path class="contact-icon--phone" d="M436,462 Q437,472 448,475"/>
      <text class="contact-phone" x="462" y="479">555-201-4836</text>
      <circle class="contact-icon--web" cx="444" cy="510" r="13"/>
      <path class="contact-icon--web" d="M431,510 H457 M444,497 Q436,510 444,523 Q452,510 444,497"/>
      <text class="contact-web" x="468" y="519">www.brightmarkpro.com</text>
    </g>
  </svg>
</main>
</body>
</html>
```